Fun but professional website required for school teaching consultancy.

Dear Designers,

I have an interesting brief for you. My client is a skilled teacher who is looking to promote her consultancy that provides bespoke training and support to other teachers.

She would like a website that promotes her philosophy for working with children, which is essentially that she wants to create a fun and creative learning environment for them, whilst maintaining the professionalism that is also required to succeed. Representation of the balance between these two points is crucial to the design.

Typically these kind of websites are pretty boring so we need something fun and vibrant, not uninviting ie those typical images of a teacher sat behind a desk or anything overly formal.

Here is an example of what we do not want: http://www.brightmarlowtutors.co.uk/ - in this one although my client liked the layout, she hated the graphics.

Here is a website that she really liked and captured the vibe of what she is trying to promote about herself: http://www.pennyvalekidsplace.com/ - this design indicates fun with learning, happy kids, lively colours and still has a professional feel as well.

If you have any further questions, please ask

Many thanks,

Gareth

PS Enclosed please find a whole bunch of resources (including site map) for this project. My client has supplied graphics, page content and plenty of visuals so hopefully this will make things easier
Updates

To all designers,

Thanks all your designs. Just to let you all know they have been sent to the client and I will supply feedback to you all individually when I get it.

Many thanks,
Gareth

Hi all,

We've had loads of designs for this project so thanks to you all very much. If there is any feedback to pass on, I will do this directly. Right now, all designs have been liked and are in the running. My client is going through them all and will make a decision on the deadline date which is the 10th May.
If you don't hear from me before then, it's simply because no alterations have been requested.

Many thanks.
Gareth

Industry/Entity Type

Training

```html
<!DOCTYPE html>
<html lang="en">
<head>
<meta charset="utf-8">
<title>Brightway – School Teaching Consultancy</title>
<link href="https://fonts.googleapis.com/css2?family=Open+Sans:wght@400;600;700&display=swap" rel="stylesheet">
<style>
:root{
  --blue:#2d8fd5;
  --blue-dark:#1f6fae;
  --grey-band:#5d6166;
  --panel:#dfe2e5;
  --panel-head:#8c9197;
  --ink:#3d4045;
  --muted:#8a8f95;
  --rule:#e3e5e8;
  --green:#8cc63f;
  --footer:#3b3e42;
  --footer-deep:#2f3236;
  --footer-text:#b9bcc0;
  --page:#f2f3f4;
}
*{box-sizing:border-box;margin:0;padding:0}
html,body{width:732px;height:1200px;overflow:hidden}
body{font-family:"Open Sans",Arial,sans-serif;color:var(--ink);background:var(--page);position:relative;font-size:10px}
.abs{position:absolute}
.header{left:0;top:0;width:732px;height:66px;background:#fff}
.brand{left:74px;top:8px;display:flex;align-items:center;gap:8px}
.brand-mark{width:40px;height:40px;background:var(--blue)}
.brand-name{font-weight:700;font-size:14px;color:var(--blue)}
.util{right:70px;top:6px;display:flex;gap:6px}
.util span{display:block;width:60px;height:14px;border:1px solid var(--rule);font-size:6px;line-height:12px;padding-left:4px;color:var(--muted)}
.nav{left:358px;top:38px;display:flex;gap:17px;font-size:8.5px;font-weight:600;color:var(--ink);text-transform:uppercase}
.nav a{color:inherit;text-decoration:none}
.band-phone{left:66px;top:78px;width:220px;height:40px;background:var(--blue);color:#fff;font-weight:600;font-size:14px;display:flex;align-items:center;gap:10px;padding-left:14px}
.band-strip{left:280px;top:84px;width:386px;height:28px;background:var(--grey-band);color:#fff;font-size:11px;display:flex;align-items:center;justify-content:flex-end;padding-right:14px}
.band-strip b{color:#6cc0ff;margin-left:4px}
.main{left:66px;top:126px;width:600px;height:832px;background:#fff}
.hero{left:66px;top:134px;width:402px;height:232px;background:linear-gradient(135deg,#d8b59a,#6f9fc9 55%,#e7d3bf)}
.hero-cap{left:66px;top:366px;width:402px;height:54px;background:#2f3a44;color:#fff;padding:8px 10px}
.hero-cap h3{font-size:10px;font-weight:700}
.hero-cap p{font-size:6.5px;color:#c8ced4;margin-top:3px;line-height:1.4}
.search{left:478px;top:134px;width:186px;height:208px;background:var(--panel)}
.search h3{background:var(--panel-head);color:#fff;font-size:10px;font-weight:700;padding:8px 10px}
.search .field{margin:8px 10px 0;height:20px;background:#fff;border:1px solid #cdd1d5;font-size:6.5px;color:var(--muted);line-height:18px;padding-left:6px}
.btn{display:inline-block;background:var(--green);color:#fff;font-size:7px;padding:4px 12px}
.search .btn{margin:10px 10px 0}
.h2{font-size:11px;font-weight:700;color:var(--blue-dark)}
.rule{height:1px;background:var(--rule)}
.photo{background:linear-gradient(135deg,#9fc2df,#d9b894)}
.copy{font-size:7px;color:var(--muted);line-height:1.45}
.links{list-style:none}
.links li{font-size:7.5px;color:var(--ink);height:24px;line-height:24px;border-bottom:1px solid var(--rule);display:flex;align-items:center;gap:6px}
.links li::before{content:"";width:6px;height:6px;border-radius:50%;background:var(--blue)}
.footer{left:0;top:958px;width:732px;height:242px;background:var(--footer)}
.news-tab{left:466px;top:958px;width:200px;height:30px;background:var(--blue);color:#fff;font-size:10px;font-weight:700;display:flex;align-items:center;justify-content:center}
.news-field{left:490px;top:1002px;width:140px;height:16px;background:#fff}
.news-go{left:634px;top:1002px;width:32px;height:16px;background:var(--panel-head);color:#fff;font-size:7px;text-align:center;line-height:16px}
.foot-h{font-size:9px;font-weight:700;color:#fff}
.foot-list{list-style:none}
.foot-list li{font-size:7px;color:var(--footer-text);height:18px;line-height:18px;display:flex;align-items:center;gap:6px}
.foot-list li::before{content:"";width:4px;height:4px;background:var(--footer-text)}
.pp{display:flex;gap:6px;margin-bottom:8px}
.pp .thumb{width:34px;height:24px;background:linear-gradient(135deg,#8aa7c0,#c9a789)}
.pp p{font-size:6.5px;color:var(--footer-text);line-height:1.4}
.cf-field{width:100px;height:14px;background:#fff;margin-bottom:6px}
.cf-area{width:140px;height:40px;background:#fff}
.bottom{left:0;top:1168px;width:732px;height:32px;background:var(--footer-deep);color:var(--footer-text);font-size:6.5px;padding:12px 96px}
</style>
</head>
<body>
<header class="abs header"></header>
<div class="abs brand"><span class="brand-mark"></span><span class="brand-name">Brightway</span></div>
<div class="abs util"><span>Search site</span><span>Member login</span></div>
<nav class="abs nav"><a>Home</a><a>About</a><a>Course</a><a>Progressive</a><a>Blog</a><a>Contact us</a></nav>

<div class="abs band-strip">Admission Open for 2012 click here to <b>Get Form</b></div>
<div class="abs band-phone">
  <svg width="14" height="14" viewBox="0 0 24 24" aria-hidden="true"><path fill="#fff" d="M6.6 10.8a15 15 0 0 0 6.6 6.6l2.2-2.2c.3-.3.7-.4 1-.2 1.1.4 2.3.6 3.6.6.6 0 1 .4 1 1V20c0 .6-.4 1-1 1A17 17 0 0 1 3 4c0-.6.4-1 1-1h3.5c.6 0 1 .4 1 1 0 1.3.2 2.5.6 3.6.1.3 0 .7-.2 1z"/></svg>
  1-800-555-0142
</div>

<main class="abs main"></main>
<div class="abs hero" role="img" aria-label="Teacher and young pupils gathered around a globe"></div>
<div class="abs hero-cap"><h3>A Student reading</h3><p>Pupils explore the world together in a bright, friendly classroom where every question is welcomed and every idea counts.</p></div>

<aside class="abs search">
  <h3>Search Course</h3>
  <div class="field">Course name</div>
  <div class="field">All course categories</div>
  <div class="field">Choose a location</div>
  <div class="field">Select course start date</div>
  <span class="btn">Search</span>
</aside>

<div class="abs h2" style="left:66px;top:445px">Welcome to My College</div>
<div class="abs rule" style="left:66px;top:466px;width:600px"></div>
<div class="abs photo" style="left:66px;top:483px;width:128px;height:54px" role="img" aria-label="Child swimming in a pool"></div>
<p class="abs copy" style="left:206px;top:483px;width:260px">Learning works best when it feels like play. We help teachers build creative, joyful classrooms while keeping the structure and standards that let every child grow and succeed at school.</p>

<div class="abs h2" style="left:66px;top:580px">Campus Tour</div>
<div class="abs rule" style="left:66px;top:601px;width:380px"></div>
<svg class="abs" style="left:420px;top:582px" width="26" height="10" aria-hidden="true"><rect x="0" y="0" width="11" height="10" fill="#d5d8db"/><rect x="14" y="0" width="11" height="10" fill="#d5d8db"/><path d="M7 2 4 5l3 3M18 2l3 3-3 3" stroke="#fff" fill="none"/></svg>
<div class="abs photo" style="left:66px;top:610px;width:178px;height:98px" role="img" aria-label="Children playing outdoors"></div>
<div class="abs photo" style="left:261px;top:610px;width:178px;height:98px;background:linear-gradient(135deg,#7fb0d9,#e0b36a)" role="img" aria-label="Pupils on the playground climbing frame"></div>
<p class="abs copy" style="left:66px;top:714px;width:178px">Take a look around our grounds and see where children learn.</p>
<p class="abs copy" style="left:261px;top:714px;width:178px">Bright spaces made for play, talk and shared learning.</p>

<div class="abs h2" style="left:481px;top:580px">Quick Links</div>
<div class="abs rule" style="left:481px;top:601px;width:185px"></div>
<ul class="abs links" style="left:481px;top:606px;width:185px">
  <li>Our Philosophy</li><li>Training Sessions</li><li>Bespoke Support Packages</li><li>Classroom Resources</li><li>Workshops and Events</li><li>Meet the Consultant</li><li>Book a Consultation</li>
</ul>

<div class="abs h2" style="left:66px;top:858px">Campus Event</div>
<div class="abs rule" style="left:66px;top:879px;width:600px"></div>
<div class="abs photo" style="left:66px;top:888px;width:107px;height:62px" role="img" aria-label="Children at a sports day"></div>
<div class="abs photo" style="left:189px;top:888px;width:107px;height:62px;background:linear-gradient(135deg,#c9c5bd,#7a95b0)" role="img" aria-label="Pupils at an outdoor event"></div>
<div class="abs photo" style="left:312px;top:888px;width:107px;height:62px;background:linear-gradient(135deg,#5e8fd0,#e4a24f)" role="img" aria-label="Kids on a bouncy castle"></div>
<div class="abs photo" style="left:435px;top:888px;width:107px;height:62px;background:linear-gradient(135deg,#b5b8bd,#8c7b6a)" role="img" aria-label="Group of pupils in a hall"></div>
<div class="abs photo" style="left:558px;top:888px;width:107px;height:62px;background:linear-gradient(135deg,#e1c06a,#5fa3d4)" role="img" aria-label="Children smiling in class"></div>

<footer class="abs footer"></footer>
<div class="abs news-tab">Newsletter Signup</div>
<div class="abs rule" style="left:66px;top:994px;width:600px;background:#4a4e53"></div>
<div class="abs news-field"></div>
<div class="abs news-go">Go</div>

<div class="abs" style="left:96px;top:1030px">
  <div class="foot-h">Recent Posts</div>
  <ul class="foot-list" style="margin-top:8px"><li>Lorem ipsum dolor sit</li><li>Creative lessons today</li><li>Play based learning</li><li>Tips for new teachers</li></ul>
</div>
<div class="abs" style="left:272px;top:1030px">
  <div class="foot-h">Popular Posts Widget</div>
  <div style="margin-top:10px">
    <div class="pp"><span class="thumb" role="img" aria-label="Post thumbnail"></span><p>Making maths fun<br>in the classroom</p></div>
    <div class="pp"><span class="thumb" role="img" aria-label="Post thumbnail"></span><p>Outdoor learning<br>ideas for spring</p></div>
    <div class="pp"><span class="thumb" role="img" aria-label="Post thumbnail"></span><p>Reading corners<br>that kids love</p></div>
  </div>
</div>
<div class="abs" style="left:512px;top:1030px">
  <div class="foot-h">Contact Form</div>
  <div style="margin-top:10px"><div class="cf-field"></div><div class="cf-field"></div><div class="cf-area"></div></div>
  <span class="btn" style="margin-top:6px;margin-left:100px">Submit</span>
</div>
<div class="abs bottom">© 2012 Brightway. All Rights Reserved</div>
</body>
</html>
```